Design a corporate looking website for Harbourline Funding

Need design only WordPress mock up for Harbourline Funding who provides short term finance solutions to other businesses. We need a corporate looking website that depicts a trustworthy, Dynamic fast acting company.
Visit http://k7.pagelantern-demo.net/ for current mock up We need something like e this but not the same with a design that depicts corporate with more colour and images, needs to install trust and fast action. Please feel free to change the layout as I am not wedded to current design but am happy with what on the landing page.

Target Market(s)

Small to medium sized Businesses

Industry/Entity Type

Finance

Number of Pages Required

1 page

Font styles to use
Sans Serif

Requirements
Must have
• Design Landing pages in WordPress
• Visit http://k7.pagelantern-demo.net/ for current mock up need Layout like this but with a design that depicts corporate with more colour and images, needs to install trust and fast action. Please feel free to change the layout as I am not happy with current design but am wedded to what on the landing page.
Should not have
• any copyright material on it.

```html
<!DOCTYPE html>
<html lang="en">
<head>
<meta charset="utf-8">
<title>Harbourline Funding</title>
<link href="https://fonts.googleapis.com/css2?family=Open+Sans:wght@400;600;700&display=swap" rel="stylesheet">
<style>
:root{
  --blue:#1b9ad8;
  --blue-light:#4aa9dc;
  --nav:#2e3238;
  --ink:#2b2b2b;
  --text:#555;
  --grey-bg:#efefef;
  --strip:#e3e8ec;
  --btn-grey:#7c7e80;
  --btn-light:#e6e8ea;
  --green:#45ad4c;
  --red:#e4392b;
  --teal:#1fb1c9;
  --white:#fff;
}
*{box-sizing:border-box;margin:0;padding:0}
html,body{width:1200px;height:3448px;overflow:hidden;background:var(--white)}
body{font-family:"Open Sans",sans-serif;color:var(--text);position:relative}
.abs{position:absolute}

/* header */
.site-header{left:0;top:0;width:1200px;height:120px;background:var(--white)}
.brand{left:104px;top:34px;display:flex;align-items:center;gap:12px}
.brand-dot{width:40px;height:40px;border-radius:50%;background:var(--blue)}
.brand-name{font-size:26px;font-weight:700;color:var(--nav)}
.search{left:800px;top:39px;width:299px;height:42px;border:1px solid #d8d8d8;border-radius:6px;display:flex;align-items:center;justify-content:space-between;padding:0 16px;font-size:13px;color:#aaa}

.main-nav{left:0;top:120px;width:1200px;height:59px;background:var(--nav);display:flex;align-items:center;padding-left:92px;gap:0}
.main-nav a{color:var(--white);text-decoration:none;font-size:12px;text-transform:uppercase;padding:0 12px;height:59px;line-height:59px;position:relative}
.main-nav a.active{color:var(--blue-light)}
.main-nav a.active::after{content:"";position:absolute;left:12px;right:12px;bottom:16px;height:2px;background:var(--blue-light)}

.tagline-band{left:0;top:179px;width:1200px;height:120px;background:var(--blue)}
.tagline-band::after{content:"";position:absolute;left:100px;bottom:-14px;border-left:16px solid transparent;border-right:16px solid transparent;border-top:14px solid var(--blue)}
.tagline{left:92px;top:28px;color:var(--white);font-size:27px;line-height:34px}
.tagline strong{font-weight:700}
.btn-outline{left:943px;top:39px;width:156px;height:42px;border:1px solid var(--white);border-radius:3px;color:var(--white);font-size:12px;text-transform:uppercase;display:flex;align-items:center;justify-content:center}

.hero{left:0;top:299px;width:1200px;height:644px;background:linear-gradient(180deg,#eceef0 0%,#d3d6d9 45%,#a88d55 80%,#6b5a3a 100%)}

.thumb-strip{left:0;top:943px;width:1200px;height:121px;background:var(--strip)}
.thumb{top:7px;width:197px;height:101px}
.t1{left:172px;background:linear-gradient(135deg,#f2f2f2,#b9a57b)}
.t2{left:391px;background:linear-gradient(135deg,#e9e2d8,#c89b62)}
.t3{left:609px;background:linear-gradient(135deg,#f1f1f1,#a7b08e)}
.t4{left:828px;background:linear-gradient(135deg,#6a9bc4,#d9c2a8)}
.arrow{top:44px}

/* about */
.about-kicker{left:0;top:1104px;width:1200px;text-align:center;color:var(--blue);font-size:30px}
.about-title{left:0;top:1142px;width:1200px;text-align:center;color:var(--ink);font-size:35px;font-weight:400}
.about-text{left:110px;top:1212px;width:980px;text-align:center;font-size:14px;line-height:22px}
.rule{left:99px;top:1298px;width:1000px;height:1px;background:#e2e2e2}

.service{top:1340px;width:320px}
.service .icon{position:absolute;left:0;top:0;width:56px;height:56px;border-radius:50%;display:flex;align-items:center;justify-content:center}
.service h3{position:absolute;left:85px;top:12px;font-size:15px;font-weight:600;color:var(--ink);white-space:nowrap}
.service .line{position:absolute;left:85px;top:42px;width:235px;height:1px;background:#e2e2e2}
.service p{position:absolute;left:85px;top:52px;width:235px;font-size:12.5px;line-height:24px}
.service .btn{position:absolute;left:85px;top:205px;width:115px;height:42px;border-radius:3px;font-size:12px;display:flex;align-items:center;justify-content:center}
.btn-light{background:var(--btn-light);color:#777;border:1px solid #d9dcdf}
.btn-dark{background:var(--btn-grey);color:var(--white)}
.dots{left:566px;top:1644px;display:flex;gap:7px}
.dots span{width:10px;height:10px;border-radius:50%;background:#d6d6d6}
.dots span.on{background:#8b8d90}

/* why */
.why{left:0;top:1711px;width:1200px;height:386px;background:var(--grey-bg)}
.why-photo{left:99px;top:57px;width:471px;height:269px;background:linear-gradient(135deg,#e9ecef 0%,#c9cfd6 50%,#3a4350 100%)}
.why-title{left:616px;top:58px;font-size:32px;color:var(--ink);font-weight:400}
.why-text{left:616px;top:114px;width:483px;font-size:13px;line-height:24px}
.why-btn{top:274px;height:41px;border-radius:3px;color:var(--white);font-size:12px;display:flex;align-items:center;justify-content:center}

/* steps */
.steps-title{left:0;top:2131px;width:1200px;text-align:center;color:var(--ink);font-size:32px;font-weight:400}
.step-ring{top:2222px;width:176px;height:176px;border-radius:50%;border:5px solid var(--blue-light);background:var(--white);display:flex;align-items:flex-start;justify-content:center;padding-top:62px;font-size:56px;font-weight:700;color:var(--blue-light)}
.step-ring.green{border-color:var(--green);color:var(--green)}
.step-bar{top:2387px;width:315px;height:51px;background:var(--blue-light);color:var(--white);font-size:16px;font-weight:600;display:flex;align-items:center;justify-content:center}
.step-bar.green{background:var(--green)}
.steps-note{left:0;top:2478px;width:1200px;text-align:center;font-size:13px}
.btn-start{left:543px;top:2527px;width:115px;height:42px;background:var(--btn-grey);color:var(--white);border-radius:3px;font-size:12px;display:flex;align-items:center;justify-content:center}

/* testimonial */
.quote-band{left:0;top:2622px;width:1200px;height:379px;background:var(--blue)}
.quote-photo{left:471px;top:0;width:729px;height:379px;background:linear-gradient(180deg,#0f3a6c 0%,#3e6f9c 45%,#b9c8d6 100%)}
.quote-card{left:99px;top:57px;width:658px;height:262px;background:var(--white);padding:48px 48px 0 48px}
.quote-card h4{color:var(--blue);font-size:20px;font-weight:600}
.quote-card blockquote{margin-top:32px;font-size:13px;line-height:24px;font-style:italic}
.quote-card cite{display:block;text-align:right;margin-top:24px;color:var(--green);font-size:16px;font-style:normal;font-weight:600}

/* footer */
.footer-brand{left:104px;top:3033px;display:flex;align-items:center;gap:12px}
.footer-brand .brand-dot{background:#8b8d90}
.footer-brand .brand-name{color:#6f7276}
.copyright{left:800px;top:3044px;width:299px;text-align:right;font-size:13px;color:#444}
</style>
</head>
<body>

<header class="site-header abs">
  <div class="brand abs"><span class="brand-dot"></span><span class="brand-name">Harbourline Funding</span></div>
  <div class="search abs"><span>Search</span>
    <svg width="16" height="16" viewBox="0 0 16 16"><circle cx="6.5" cy="6.5" r="5" fill="none" stroke="#333" stroke-width="2"/><line x1="10" y1="10" x2="15" y2="15" stroke="#333" stroke-width="2"/></svg>
  </div>
</header>

<nav class="main-nav abs">
  <a class="active">Home</a><a>Services</a><a>Why Harbourline</a><a>Investors</a><a>About Us</a><a>Contact Us</a><a>Members Login</a>
</nav>

<section class="tagline-band abs">
  <div class="tagline abs">Business Taken<br>to The <strong>New Heights</strong></div>
  <div class="btn-outline abs">Read More</div>
</section>

<div class="hero abs" role="img" aria-label="Hand placing a small white toy car on stacks of gold coins"></div>

<div class="thumb-strip abs">
  <svg class="arrow abs" style="left:96px" width="30" height="30" viewBox="0 0 30 30"><path d="M26 15H6M13 7l-8 8 8 8" fill="none" stroke="#1b9ad8" stroke-width="3"/></svg>
  <div class="thumb t1 abs" role="img" aria-label="Toy car on coin stacks"></div>
  <div class="thumb t2 abs" role="img" aria-label="Hand stacking coins"></div>
  <div class="thumb t3 abs" role="img" aria-label="Banknotes passed between hands"></div>
  <div class="thumb t4 abs" role="img" aria-label="Two men discussing finances"></div>
  <svg class="arrow abs" style="left:1075px" width="30" height="30" viewBox="0 0 30 30"><path d="M4 15h20M17 7l8 8-8 8" fill="none" stroke="#1b9ad8" stroke-width="3"/></svg>
</div>

<h2 class="about-kicker abs">About us</h2>
<h1 class="about-title abs">Present yourself to the whole world</h1>
<p class="about-text abs">Contrary to popular belief, Lorem Ipsum is not simply random text. It has roots in a piece of classical Latin literature from 45 BC, making it over 2000 years old. Daniel Okonkwo, a Latin professor at Westbrook College in Oregon</p>
<div class="rule abs"></div>

<article class="service abs" style="left:99px">
  <div class="icon" style="background:var(--teal)"><svg width="24" height="24" viewBox="0 0 24 24"><path d="M3 12L12 4l9 8h-3v8h-5v-5h-2v5H6v-8z" fill="#fff"/></svg></div>
  <h3>Residential Real Estate Agents</h3><div class="line"></div>
  <p>Whether you're a Residential Real Estate Agency or Agent we understand that with residential real estate transactions settling on average in 42 days that your well earned and outstanding commissions ...</p>
  <div class="btn btn-light">Read More</div>
</article>
<article class="service abs" style="left:441px">
  <div class="icon" style="background:var(--green)"><svg width="24" height="24" viewBox="0 0 24 24"><g stroke="#fff" stroke-width="2.5" stroke-linecap="round"><line x1="12" y1="3" x2="12" y2="7"/><line x1="12" y1="17" x2="12" y2="21"/><line x1="3" y1="12" x2="7" y2="12"/><line x1="17" y1="12" x2="21" y2="12"/><line x1="5.6" y1="5.6" x2="8.5" y2="8.5"/><line x1="15.5" y1="15.5" x2="18.4" y2="18.4"/><line x1="5.6" y1="18.4" x2="8.5" y2="15.5"/><line x1="15.5" y1="8.5" x2="18.4" y2="5.6"/></g></svg></div>
  <h3>Commercial Real Estate Agents</h3><div class="line"></div>
  <p>Whether you're a Commercial Real Estate Agency or Agent we understand that with commercial real estate transactions settling at all different periods that well earned and outstanding commissions ...</p>
  <div class="btn btn-dark">Read More</div>
</article>
<article class="service abs" style="left:784px">
  <div class="icon" style="background:var(--red)"><svg width="24" height="24" viewBox="0 0 24 24"><g fill="none" stroke="#fff" stroke-width="2.2"><ellipse cx="12" cy="7" rx="7" ry="3"/><path d="M5 7v5c0 1.7 3.1 3 7 3s7-1.3 7-3V7M5 12v5c0 1.7 3.1 3 7 3s7-1.3 7-3v-5"/></g></svg></div>
  <h3>Mortgage &amp; Finance Brokers</h3><div class="line"></div>
  <p>Whether you're a mortgage broker focusing on home loans or a finance broker operating in different area's of finance we have a deep understanding of your industry and the nuances involved, especially ...</p>
  <div class="btn btn-light">Read More</div>
</article>
<div class="dots abs"><span></span><span></span><span class="on"></span><span></span></div>

<section class="why abs">
  <div class="why-photo abs" role="img" aria-label="Business team gathered around a laptop in a bright office"></div>
  <h2 class="why-title abs">Why Harbourline Funding</h2>
  <p class="why-text abs">At Harbourline Funding our aim is to provide immediate commission advance solutions for all industries. Our background is sales, property and finance and we understand the issues faced with Small to medium Businesses, Agents, contractors and consultants who earn commissions. Unforeseen expenses, inconstant sales, holiday periods, sickness, taxation bills and job changes can all have an effect on a sales and commission flow.</p>
  <div class="why-btn abs" style="left:616px;width:115px;background:var(--btn-grey)">Read More</div>
  <div class="why-btn abs" style="left:745px;width:166px;background:var(--blue-light)">Our Pricing Guaranteed</div>
  <div class="why-btn abs" style="left:927px;width:172px;background:var(--btn-grey)">Our Loyalty Program</div>
</section>

<h2 class="steps-title abs">3 Easy Steps To a Stress Free Solution</h2>
<div class="step-ring abs" style="left:170px">01</div>
<div class="step-ring green abs" style="left:511px">02</div>
<div class="step-ring abs" style="left:857px">03</div>
<div class="step-bar abs" style="left:99px">Call or click</div>
<div class="step-bar green abs" style="left:441px">Fill out &amp; Sign</div>
<div class="step-bar abs" style="left:784px">Funds in bank in 4 hours</div>
<p class="steps-note abs">A hassle free finance solution that grows as your business grows</p>
<div class="btn-start abs">Start Now</div>

<section class="quote-band abs">
  <div class="quote-photo abs" role="img" aria-label="Businessman launching a paper plane against a blue sky"></div>
  <div class="quote-card abs">
    <h4>What people say about us</h4>
    <blockquote>" The service was beyond my expectations. But please, replace this with an actual customer testimonial, this is just for testing purposes ".</blockquote>
    <cite>Clara Whitfield, Brightmoor Goods LLC</cite>
  </div>
</section>

<footer>
  <div class="footer-brand abs"><span class="brand-dot"></span><span class="brand-name">Harbourline Funding</span></div>
  <p class="copyright abs">Copyright © 2016, All Right Reserved</p>
</footer>

</body>
</html>
```